Explosive, chemical reaction of creativity!

Web design for a digital marketing company. The unconventional is encouraged!
This is for a cool, young, geographically diverse company (makerflock... you are all part of our team!!!)... we build websites but our real specialty is "search experience optimization".... creating conversion focused content, SEO (including content), and social media.

Target Market(s)

small to medium size businesses, law firms, medical practices, municipalities

Industry/Entity Type

Marketing

Number of Pages Required

2 page

Requirements
Must have
• WOW
• something different and special... we've been playing with a science theme (www.plumridgeweb.marketing) but we are open to different looks, layouts, etc.
• we nee a homepage design and an interior page design
• content needs to include: Marketing Catalysts (about us), Our Formula (services), Chemical Reactions(Results/Our Clients),
• FREE Digital Litmus Test
• Let us put together an objective snapshot of your digital presence for you.
Nice to have
• we are open to the use of background video (chemical reaction???)
• we are open to cool and different imagery
Should not have
• template look like most other websites

```html
<!DOCTYPE html>
<html lang="en">
<head>
<meta charset="utf-8">
<title>Plumridge Web Marketing</title>
<link href="https://fonts.googleapis.com/css2?family=Open+Sans:wght@300;400;600;700&display=swap" rel="stylesheet">
<style>
:root{
  --navy:#1d3f66;
  --navy-deep:#163352;
  --blue:#2b6cb3;
  --bright:#3d86d6;
  --ink:#2b2b2b;
  --muted:#666;
  --line:#d9dde2;
  --white:#fff;
  --grey-bg:#eceef0;
}
*{box-sizing:border-box;margin:0;padding:0}
html,body{width:1200px;height:3913px;overflow:hidden}
body{font-family:"Open Sans",Arial,sans-serif;color:var(--ink);background:var(--white);position:relative}

/* header */
.site-header{position:absolute;top:0;left:0;width:1200px;height:84px;background:var(--white);border-bottom:1px solid var(--line)}
.brand{position:absolute;left:100px;top:26px;display:flex;align-items:center;gap:10px}
.brand-mark{width:30px;height:30px;background:var(--blue)}
.brand-name{font-size:16px;font-weight:700;color:var(--navy);letter-spacing:.6px;text-transform:uppercase;white-space:nowrap}
.main-nav{position:absolute;right:100px;top:33px;display:flex;align-items:center;gap:32px;font-size:13px;color:var(--ink);white-space:nowrap}
.search-icon{width:14px;height:14px}

/* hero */
.hero{position:absolute;top:84px;left:0;width:1200px;height:438px;background:radial-gradient(circle at 30% 55%,#2e82d8 0%,#0f4aa0 40%,#062a6a 100%)}
.hero-brand{position:absolute;right:120px;top:120px;display:flex;align-items:center;gap:14px}
.hero-brand .brand-mark{width:48px;height:48px;background:var(--white)}
.hero-brand .brand-name{color:var(--white);font-size:30px}
.hero-tagline{position:absolute;right:120px;top:200px;text-align:right;color:var(--white);font-size:44px;font-weight:300;line-height:1.2}
.hero-arrow{position:absolute;top:285px;width:20px;height:34px}

/* section titles */
.section-title{position:absolute;left:0;right:0;display:flex;justify-content:center;align-items:center;gap:14px;font-size:27px;font-weight:600;color:var(--navy)}
.title-mark{width:26px;height:26px;background:var(--blue)}
.on-dark .section-title{color:var(--white)}
.subtitle{position:absolute;left:0;right:0;text-align:center;font-size:18px;color:#444;line-height:1.55}

/* data */
.data-copy{position:absolute;left:180px;width:840px;top:698px;text-align:center;font-size:13px;line-height:2;color:#444}
.stat{position:absolute;top:820px;width:220px;text-align:center}
.stat svg{display:block;margin:0 auto}
.stat p{margin-top:22px;font-size:13.5px;line-height:1.7;color:#444}

/* formula */
.formula{position:absolute;top:1044px;left:0;width:1200px;height:448px;background:var(--navy)}
.pillar{position:absolute;top:188px;width:260px;text-align:center;color:var(--white)}
.pillar-icon{width:76px;height:76px;margin:0 auto;background:var(--white);border:3px solid #c9d3de;display:flex;align-items:center;justify-content:center}
.pillar h3{font-size:19px;font-weight:400;margin-top:14px}
.pillar p{font-size:13px;line-height:1.85;margin-top:12px;color:#e4ebf3}

/* facts */
.fact{position:absolute;top:1618px;width:234px;height:234px;border-radius:50%;border:4px solid #cfd8e2;color:var(--white);text-align:center;box-shadow:0 4px 10px rgba(0,0,0,.18)}
.fact.dark{background:#3a5a80}
.fact.light{background:#3d7fc4}
.fact .num{font-size:50px;font-weight:300;margin-top:22px;line-height:1}
.fact svg{display:block;margin:14px auto 0}
.fact .label{font-size:12.5px;line-height:1.5;margin-top:12px;padding:0 30px}

/* litmus */
.litmus{position:absolute;top:1957px;left:0;width:1200px;height:214px;background:linear-gradient(90deg,#d6d9dd 0%,#e4e6e9 55%,#b9c7d6 80%,#8fa4bd 100%)}
.litmus h2{position:absolute;left:98px;top:52px;font-size:26px;font-weight:600;color:var(--navy)}
.litmus p{position:absolute;left:98px;top:108px;width:480px;font-size:13px;line-height:1.85;color:#555}

/* news */
.news{position:absolute;top:2171px;left:0;width:1200px;height:581px;background:var(--grey-bg)}
.card{position:absolute;top:135px;width:316px}
.card-media{height:186px;position:relative}
.card-date{position:absolute;left:0;top:0;width:64px;padding:6px 8px;background:#3e6da3;color:var(--white);font-size:13px;line-height:1.35}
.card h3{font-size:17px;font-weight:600;line-height:1.6;margin-top:18px;color:var(--ink)}
.card .meta{font-size:12.5px;margin-top:10px;color:#555}
.card .meta b{font-weight:400;color:var(--blue)}
.card p{font-size:12.5px;line-height:1.75;margin-top:12px;color:#555}
.card .more{display:block;text-align:right;font-size:12.5px;color:var(--blue);margin-top:10px}

/* cta */
.cta{position:absolute;top:2752px;left:0;width:1200px;height:332px;background:linear-gradient(180deg,#2a6db3 0%,#1d5594 100%)}
.cta-photo{position:absolute;left:0;top:0;width:620px;height:332px;background:linear-gradient(120deg,#1b1c20 0%,#3a3030 45%,#2a2c33 100%);clip-path:polygon(0 0,100% 0,72% 100%,0 100%)}
.cta h2{position:absolute;left:628px;top:40px;width:500px;font-size:23px;font-weight:600;line-height:1.4;color:var(--white)}
.cta ul{position:absolute;left:628px;top:144px;width:480px;list-style:none;font-size:12.5px;line-height:1.75;color:#e8eef6}
.cta li{position:relative;padding-left:28px;margin-bottom:12px}
.cta li::before{content:"";position:absolute;left:2px;top:8px;width:7px;height:7px;border-radius:50%;background:var(--white)}
.btn-outline{position:absolute;padding:8px 22px;font-size:15px;border:2px solid;border-radius:3px;background:transparent}
.cta .btn-outline{left:632px;top:274px;color:var(--white);border-color:var(--white);font-weight:600}

/* contact */
.field{position:absolute;left:143px;width:457px;height:50px;border:1px solid var(--line);padding:0 18px;font-size:13px;color:#999;display:flex;align-items:center;justify-content:space-between}
.field svg{width:18px;height:18px}
.message{position:absolute;left:621px;top:3209px;width:454px;height:172px;border:1px solid var(--line);padding:14px 18px;font-size:13px;color:#999}
.send{left:520px;top:3438px;color:var(--ink);border-color:#aab4c0;border-width:1px;font-weight:600}
.contact-line{position:absolute;display:flex;align-items:center;gap:16px;font-size:15px;color:#444}
.ring-icon{width:40px;height:40px;border-radius:50%;border:1px solid #bbb;display:flex;align-items:center;justify-content:center}

/* footer */
.site-footer{position:absolute;top:3666px;left:0;width:1200px;height:247px;background:linear-gradient(180deg,#1d5594 0%,#133b6b 100%);border-top:5px solid #173e6b}
.social{position:absolute;top:46px;left:0;right:0;display:flex;justify-content:center;gap:26px}
.social span{width:54px;height:54px;border-radius:50%;border:3px solid var(--white)}
.foot-nav{position:absolute;top:150px;left:0;right:0;text-align:center;font-size:13px;color:var(--white);word-spacing:4px}
.copyright{position:absolute;top:198px;left:0;right:0;text-align:center;font-size:12px;color:#dce6f2}
</style>
</head>
<body>

<header class="site-header">
  <div class="brand"><span class="brand-mark"></span><span class="brand-name">Plumridge Web Marketing</span></div>
  <nav class="main-nav">
    <span>Home</span><span>Marketing Catalysts</span><span>Our Formula</span><span>Chemical Reactions</span><span>Contact us</span>
    <svg class="search-icon" viewBox="0 0 14 14"><circle cx="6" cy="6" r="4.5" fill="none" stroke="#1d3f66" stroke-width="2"/><line x1="9.3" y1="9.3" x2="13" y2="13" stroke="#1d3f66" stroke-width="2"/></svg>
  </nav>
</header>

<section class="hero" role="img" aria-label="Glowing blue laboratory flask with swirling liquid on a molecular background">
  <svg class="hero-arrow" style="left:40px" viewBox="0 0 20 34"><polyline points="17,2 3,17 17,32" fill="none" stroke="#fff" stroke-width="3"/></svg>
  <svg class="hero-arrow" style="right:40px" viewBox="0 0 20 34"><polyline points="3,2 17,17 3,32" fill="none" stroke="#fff" stroke-width="3"/></svg>
  <div class="hero-brand"><span class="brand-mark"></span><span class="brand-name">Plumridge Web Marketing</span></div>
  <div class="hero-tagline">It's not rocket science, it's<br>Plumridge Web science!</div>
</section>

<section class="data">
  <h2 class="section-title" style="top:556px"><span class="title-mark"></span>Using data for success</h2>
  <p class="subtitle" style="top:615px">Search Engine Optimization has been replaced with<br>Search Experience Optimization</p>
  <p class="data-copy">SALES is the end result of everything we do. It is why companies exist. It's why we market. It's why your business is online. Our job is to help you maximize your opportunity online to build your brand, get found by new customers and, ultimately, generate SALES! There's been a lot of talk the last few years about SEO, Search Engine Optimization. We believe that Search Engine Optimization has now been replaced with Search Experience Optimization. That's right, we said it.</p>

  <div class="stat" style="left:153px">
    <svg width="110" height="110" viewBox="0 0 110 110"><circle cx="55" cy="55" r="50" fill="none" stroke="#e3e6ea" stroke-width="3"/><circle cx="55" cy="55" r="50" fill="none" stroke="#1d3f66" stroke-width="3" stroke-dasharray="292 314" transform="rotate(-90 55 55)"/><text x="55" y="62" text-anchor="middle" font-size="20" font-family="Open Sans,sans-serif" fill="#333">93%</text></svg>
    <p>Online experiences begin<br>with a search engine</p>
  </div>
  <div class="stat" style="left:357px">
    <svg width="110" height="110" viewBox="0 0 110 110"><circle cx="55" cy="55" r="50" fill="none" stroke="#e3e6ea" stroke-width="3"/><circle cx="55" cy="55" r="50" fill="none" stroke="#1d3f66" stroke-width="3" stroke-dasharray="220 314" transform="rotate(-90 55 55)"/><text x="55" y="62" text-anchor="middle" font-size="20" font-family="Open Sans,sans-serif" fill="#333">70%</text></svg>
    <p>Of the links search users<br>click on are organic</p>
  </div>
  <div class="stat" style="left:570px">
    <svg width="110" height="110" viewBox="0 0 110 110"><circle cx="55" cy="55" r="50" fill="none" stroke="#e3e6ea" stroke-width="3"/><circle cx="55" cy="55" r="50" fill="none" stroke="#1d3f66" stroke-width="3" stroke-dasharray="220 314" transform="rotate(-90 55 55)"/><text x="55" y="62" text-anchor="middle" font-size="20" font-family="Open Sans,sans-serif" fill="#333">70%</text></svg>
    <p>Of US population has at least one<br>social networking profile</p>
  </div>
  <div class="stat" style="left:810px">
    <svg width="110" height="110" viewBox="0 0 110 110"><circle cx="55" cy="55" r="50" fill="none" stroke="#e3e6ea" stroke-width="3"/><circle cx="55" cy="55" r="50" fill="none" stroke="#1d3f66" stroke-width="3" stroke-dasharray="157 314" transform="rotate(-90 55 55)"/><text x="55" y="62" text-anchor="middle" font-size="20" font-family="Open Sans,sans-serif" fill="#333">50%</text></svg>
    <p>Of companies are using digital<br>marketing but don't have a plan</p>
  </div>
</section>

<section class="formula on-dark">
  <h2 class="section-title" style="top:46px"><span class="title-mark" style="background:#fff"></span>The Perfect Digital Marketing Formula!</h2>
  <p class="subtitle" style="top:98px;color:#dde6f0">Get the right message in front of the right people</p>

  <div class="pillar" style="left:108px">
    <div class="pillar-icon"><svg width="50" height="50" viewBox="0 0 50 50" fill="none" stroke="#1d3f66" stroke-width="2.5"><circle cx="25" cy="25" r="21"/><ellipse cx="25" cy="25" rx="9" ry="21"/><line x1="4" y1="25" x2="46" y2="25"/><path d="M8 14h34M8 36h34"/></svg></div>
    <h3>Website</h3>
    <p>You've got 10 seconds to grab the attention of a site viewer. We build for appearance, content, and functionality. It's a conversion causal nexus!</p>
  </div>
  <div class="pillar" style="left:463px">
    <div class="pillar-icon"><svg width="50" height="50" viewBox="0 0 50 50" fill="none" stroke="#1d3f66" stroke-width="2.5"><rect x="6" y="6" width="38" height="38" rx="3"/><rect x="13" y="14" width="5" height="5" fill="#1d3f66"/><rect x="13" y="23" width="5" height="5" fill="#1d3f66"/><rect x="13" y="32" width="5" height="5" fill="#1d3f66"/><line x1="22" y1="16.5" x2="37" y2="16.5"/><line x1="22" y1="25.5" x2="37" y2="25.5"/><line x1="22" y1="34.5" x2="37" y2="34.5"/></svg></div>
    <h3>Content</h3>
    <p>Content is the most powerful element of our formula... It creates need, provokes emotion and sparks action.</p>
  </div>
  <div class="pillar" style="left:828px">
    <div class="pillar-icon"><svg width="50" height="50" viewBox="0 0 50 50" fill="none" stroke="#1d3f66" stroke-width="2.5"><circle cx="36" cy="11" r="6"/><circle cx="13" cy="25" r="6"/><circle cx="36" cy="39" r="6"/><line x1="18" y1="22" x2="31" y2="14"/><line x1="18" y1="28" x2="31" y2="36"/></svg></div>
    <h3>Social</h3>
    <p>We are obsessed with the latest trends and are always testing new ways to cultivate both following and engagement.</p>
  </div>
</section>

<section class="facts">
  <h2 class="section-title" style="top:1532px"><span class="title-mark"></span>Some Facts About Our Catalysts</h2>
  <p class="subtitle" style="top:1575px">Working together to create change</p>

  <div class="fact dark" style="left:183px">
    <div class="num">35</div>
    <svg width="52" height="42" viewBox="0 0 52 42" fill="#fff"><path d="M4 6h34v16a13 13 0 0 1-13 13h-8A13 13 0 0 1 4 22z"/><path d="M38 10h5a6 6 0 0 1 0 12h-5v-4h5a2 2 0 0 0 0-4h-5z"/><rect x="0" y="37" width="46" height="4" rx="2"/></svg>
    <div class="label">Years Combined Marketing Experience</div>
  </div>
  <div class="fact light" style="left:379px">
    <div class="num">10</div>
    <svg width="30" height="46" viewBox="0 0 30 46" fill="none" stroke="#fff" stroke-width="3"><rect x="2" y="2" width="26" height="42" rx="4"/><line x1="11" y1="38" x2="19" y2="38"/></svg>
    <div class="label">Years Search Engine Optimization Experience</div>
  </div>
  <div class="fact dark" style="left:574px">
    <div class="num">234</div>
    <svg width="44" height="46" viewBox="0 0 44 46" fill="#fff"><path d="M22 2l9 11H13zM22 10l13 14H9zM22 20l17 16H5z"/><rect x="18" y="37" width="8" height="8"/></svg>
    <div class="label">Websites created</div>
  </div>
  <div class="fact light" style="left:770px">
    <div class="num">1</div>
    <svg width="44" height="46" viewBox="0 0 44 46" fill="#fff"><path d="M22 2l9 11H13zM22 10l13 14H9zM22 20l17 16H5z"/><rect x="18" y="37" width="8" height="8"/></svg>
    <div class="label">Amazing team</div>
  </div>
</section>

<section class="litmus" role="img" aria-label="Soft laboratory glassware with pouring liquid fading in from the right">
  <h2>FREE Digital Litmus Test</h2>
  <p>We test your site, content and social reach, then report the results plainly. Simple checks reveal exactly where your online presence can react better.</p>
</section>

<section class="news">
  <h2 class="section-title" style="top:50px"><span class="title-mark"></span>Our News Events</h2>

  <article class="card" style="left:99px">
    <div class="card-media" role="img" aria-label="Illustration of a small blue bird with a speech caption" style="background:linear-gradient(180deg,#ffffff 0%,#eef3f8 100%);border:1px solid var(--line)"><span class="card-date">May 17<br>2016</span></div>
    <h3>A Little Bird Told Me – 5 Reasons for Tweeting</h3>
    <div class="meta"><b>Added on May 17, 2016</b> at 12:41</div>
    <p>There's a thin red line between social media use and networking. Sometimes the two merge into a perfect harmony of conversation and resolution.</p>
    <span class="more">[ Read more ]</span>
  </article>
  <article class="card" style="left:443px">
    <div class="card-media" role="img" aria-label="Photo of a man wearing augmented reality glasses" style="background:linear-gradient(135deg,#6d7f96 0%,#b7c4d3 50%,#54657b 100%)"><span class="card-date">May 17<br>2016</span></div>
    <h3>The Revolution Will Now Be Optimized</h3>
    <div class="meta"><b>Added on May 03, 2016</b> at 15:41</div>
    <p>Every new device changes how people search. We keep your brand ready for the next screen, the next habit and the next idea.</p>
    <span class="more">[ Read more ]</span>
  </article>
  <article class="card" style="left:788px">
    <div class="card-media" role="img" aria-label="Dark screen showing a loading spinner under a large headline" style="background:linear-gradient(180deg,#1c1c1c 0%,#3a3a3a 100%)"><span class="card-date">May 17<br>2016</span></div>
    <h3>Take Your Business to the Next Level : Summit Edition</h3>
    <div class="meta"><b>Added on April 08, 2016</b> at 13:18</div>
    <p>Fast pages win attention. Here is what we learned at the summit about speed, search and keeping visitors long enough to convert.</p>
    <span class="more">[ Read more ]</span>
  </article>
</section>

<section class="cta">
  <div class="cta-photo" role="img" aria-label="Dramatic dark portrait photograph"></div>
  <h2>Let us put together an objective<br>snapshot of your digital presence for you</h2>
  <ul>
    <li>Our review covers your website, search visibility and content, and we explain every finding in plain language you can act on.</li>
    <li>You receive a clear plan with priorities, so your team knows which changes bring the fastest results.</li>
  </ul>
  <span class="btn-outline">Read More</span>
</section>

<section class="contact">
  <h2 class="section-title" style="top:3120px">Contact Us</h2>
  <div class="field" style="top:3209px">First &amp; Last name<svg viewBox="0 0 18 18" fill="#bbb"><circle cx="9" cy="5" r="4"/><path d="M1 18a8 8 0 0 1 16 0z"/></svg></div>
  <div class="field" style="top:3271px">Phone No.<svg viewBox="0 0 18 18" fill="#bbb"><path d="M4 1l3 4-2 2a10 10 0 0 0 6 6l2-2 4 3-2 3C8 17 1 10 1 3z"/></svg></div>
  <div class="field" style="top:3333px">Email Id *<svg viewBox="0 0 18 18" fill="none" stroke="#bbb" stroke-width="1.5"><rect x="1" y="4" width="16" height="11"/><polyline points="1,4 9,10 17,4"/></svg></div>
  <div class="message">your message</div>
  <span class="btn-outline send">Send Message</span>

  <div class="contact-line" style="left:300px;top:3520px">
    <span class="ring-icon"><svg width="14" height="20" viewBox="0 0 14 20" fill="none" stroke="#555" stroke-width="1.6"><rect x="1" y="1" width="12" height="18" rx="2"/><line x1="5" y1="16" x2="9" y2="16"/></svg></span>
    <span>Call Us :&nbsp;&nbsp; 866-310-4472 &nbsp;&nbsp;&nbsp;&nbsp;, &nbsp;&nbsp;+44 203 555 0192 &nbsp;&nbsp;&nbsp;&nbsp;, &nbsp;&nbsp;+61 2 5550 1736</span>
  </div>
  <div class="contact-line" style="left:248px;top:3586px">
    <span class="ring-icon"><svg width="18" height="14" viewBox="0 0 18 14" fill="none" stroke="#555" stroke-width="1.6"><rect x="1" y="1" width="16" height="12"/><polyline points="1,1 9,8 17,1"/></svg></span>
    <span>Email &nbsp;: &nbsp;info@plumridgeweb.com</span>
  </div>
  <div class="contact-line" style="left:600px;top:3586px">
    <span class="ring-icon"></span>
    <span>https://social.plumridgeweb.com/team</span>
  </div>
</section>

<footer class="site-footer">
  <div class="social"><span></span><span></span><span></span><span></span></div>
  <div class="foot-nav">Home &nbsp;/&nbsp; Marketing Catalysts &nbsp;/&nbsp; Our Formula &nbsp;/&nbsp; Chemical Reactions &nbsp;/&nbsp; Contact us</div>
  <div class="copyright">All Rights Reserved , Copyrights2016@companyname.com</div>
</footer>

</body>
</html>
```